Speisekarten-Design für Café
Zielgruppe
Café mit Angebot von Frühstück und Torten/Kuchen (BIO!) und Verkauf von Dekoartikeln. Zielgruppe sind sowohl Familien, als auch ältere Personen, die sich zum Kaffeeklatsch treffen. Ebenso 'Freundinnen' und junge Mütter.
In den Räumlichkeiten war schon seit 24 Jahren ein Café, die Besitzerin ist aber verstorben
Aufgabenstellung
Karte in DIN A 5 Format, da die Tische nicht so groß sind. Die erste Seite soll die 'Geschichte' der Lokalität enthalten. Keine 'bunten' Bilder (Comics) von irgendwelchen Torten und/oder Frühstücken

```html
<!DOCTYPE html>
<html lang="de">
<head>
<meta charset="utf-8">
<title>Café Fräulein Mathilde – Speisekarte</title>
<link href="https://fonts.googleapis.com/css2?family=Cinzel:wght@700&family=IM+Fell+English&family=Oswald:wght@300;500&family=Crimson+Text&display=swap" rel="stylesheet">
<style>
:root{
  --canvas:#ffffff;
  --rose:#d46a8d;
  --rose-deep:#c95a80;
  --glow:#e23d78;
  --plum:#6e1f44;
  --heading:#8c3a63;
  --ink:#4a1430;
  --ink-soft:#5c1d3c;
}
*{margin:0;padding:0;box-sizing:border-box}
html,body{width:1200px;height:1198px;overflow:hidden;background:var(--canvas)}
body{position:relative;font-family:"Oswald",sans-serif;font-weight:300;color:var(--ink)}
.panel{position:absolute;background:var(--rose);box-shadow:inset 0 0 6px 2px var(--glow);overflow:hidden}
.pattern-fill{position:absolute;inset:0;background:radial-gradient(ellipse at 50% 50%,#d77294 0%,var(--rose) 55%,var(--rose-deep) 100%)}
.frame{position:absolute;border:2px solid var(--plum)}
.cover{left:57px;top:49px;width:516px;height:516px}
.back{left:619px;top:49px;width:517px;height:516px}
.cover .frame,.back .frame{left:18px;top:17px;right:16px;bottom:16px}
.caption{position:absolute;top:574px;font-family:"Crimson Text",serif;font-size:22px;color:#111}
.brand-name{position:absolute;font-family:"Oswald",sans-serif;font-weight:500;color:var(--plum);text-align:center;white-space:nowrap;transform:translate(-50%,-50%)}
.cover .brand-name{left:260px;top:180px;font-size:30px}
.cover-title{position:absolute;left:0;right:0;top:384px;text-align:center;font-family:"Cinzel",serif;font-size:24px;color:var(--heading);letter-spacing:1px}
.portrait{position:absolute;left:196px;top:9px;width:131px;height:175px;border-radius:50%;border:5px solid #111;background:radial-gradient(ellipse at 45% 40%,#e8d9c8 0%,#b89474 45%,#4f6a66 100%);box-shadow:0 0 6px 2px var(--glow)}
.story-title{position:absolute;left:0;right:0;top:188px;text-align:center;font-family:"IM Fell English",serif;font-weight:400;font-size:31px;line-height:34px;color:var(--heading);letter-spacing:1px}
.story-text{position:absolute;left:50%;width:420px;transform:translateX(-50%);top:268px;text-align:center;font-size:10.4px;line-height:13.7px;color:var(--ink-soft)}
.contact{position:absolute;left:0;right:0;top:432px;text-align:center;font-size:10px;line-height:14px;color:var(--ink-soft)}
.spread{left:70px;top:636px;width:1033px;height:516px}
.spread .frame{left:19px;top:49px;right:23px;bottom:15px}
.spread .brand-name{font-size:13px;background:var(--rose);padding:4px 8px;top:50px}
.section-title{position:absolute;font-family:"Cinzel",serif;font-size:27px;color:var(--heading);transform:translateX(-50%);white-space:nowrap;top:96px}
.hours{position:absolute;left:259px;top:126px;font-size:9.6px;transform:translateX(-50%)}
.col{position:absolute;top:150px;font-size:8.4px;line-height:13.6px}
.col h3{font-weight:500;font-size:9px;line-height:13px;margin-top:3px}
.row{display:flex;justify-content:space-between;gap:6px}
.row .price{flex:none}
.desc{line-height:10px;display:flex;justify-content:space-between;align-items:flex-end;gap:6px}
.desc p{flex:1}
.head-row{display:flex;justify-content:space-between;gap:6px;font-weight:500;font-size:9px;line-height:11px}
.head-row span:last-child{font-weight:300}
.gap{height:9px}
</style>
</head>
<body>

<section class="panel cover">
  <div class="pattern-fill" role="img" aria-label="Gezeichnetes Muster aus Kaffeekannen, Tassen und Torten in Rosa"></div>
  <div class="frame"></div>
  <div class="brand-name">Café Fräulein Mathilde</div>
  <h1 class="cover-title">STEISEN UND GETRÄNKE</h1>
</section>
<div class="caption" style="left:57px">Titel</div>

<section class="panel back">
  <div class="pattern-fill" role="img" aria-label="Gezeichnetes Muster aus Kaffeekannen, Tassen und Torten in Rosa"></div>
  <div class="frame"></div>
  <div class="portrait" role="img" aria-label="Ovales historisches Portraitgemälde einer Dame mit schwarzer Katze"></div>
  <h2 class="story-title">Die Geschichte eines<br>ungewöhnlichen Cafés</h2>
  <p class="story-text">Vielleicht steht hier ja die ungewöghnliche Geschichte des Fräulein Mathilde und wie sie vor 70 Jahren zu dem Cafe gekommen ist. Vielleicht steht hier ja die ungewöghnliche Geschichte des Fräulein Mathilde und wie sie vor 70 Jahren zu dem Cafe gekommen ist. Vielleicht steht hier ja die ungewöghnliche Geschichte des Fräulein Mathilde und wie sie vor 70 Jahren zu dem Cafe gekommen ist. Vielleicht steht hier ja die ungewöghnliche Geschichte des Fräulein Mathilde und wie sie vor 70 Jahren zu dem Cafe gekommen ist. Vielleicht steht hier ja die ungewöghnliche Geschichte des Fräulein Mathilde und wie sie vor 70 Jahren zu dem Cafe gekommen ist. Vielleicht steht hier ja die ungewöghnliche Geschichte des Fräulein Mathilde und wie sie vor 70 Jahren zu dem Cafe gekommen ist.</p>
  <p class="contact">Café Mathilde - Am Kirchplatz 12 - 31500 Lindenau<br>Telefon 05120/5550123 - www.fraeulein-mathilde.de</p>
</section>
<div class="caption" style="left:619px">Rückseite</div>

<section class="panel spread">
  <div class="pattern-fill" role="img" aria-label="Gezeichnetes Muster aus Kaffeekannen, Tassen und Torten in Rosa"></div>
  <div class="frame"></div>
  <div class="brand-name" style="left:257px">Café Fräulein Mathilde</div>
  <div class="brand-name" style="left:774px">Café Fräulein Mathilde</div>

  <h2 class="section-title" style="left:258px">FRÜHSTÜCKS-TELLER</h2>
  <div class="hours">von 9 - 12 Uhr</div>
  <h2 class="section-title" style="left:775px">GETRÄNKE</h2>

  <div class="col" style="left:40px;width:180px">
    <h3>Die Welt des Frühstücks in deiner Hand...</h3>
    <div class="desc"><p>2 Brötchen, 2x gute Butter, 2x Marmelade, Tomate &amp; Gurke (wählen Sie aus unserer Karte weitere, genussvolle Extras)</p><span>4,90</span></div>
    <div class="desc" style="margin-top:4px"><p>Auch als <b>kleine Welt</b> mit 1 Brötchen, 1x Butter, 1x Marmelade erhältlich</p><span>3,80</span></div>
    <h3>Mediterranes Flair</h3>
    <div class="desc"><p>2x Brötchen, 2x gute Butter, ital. Aufschnitt, Tomate-Mozarella-Sticks, ital. Käseauswahl, Marmelade, Obst</p><span>9,90</span></div>
    <h3>Frühstück Fräulein Mathilde für Zwei</h3>
    <div class="desc"><p>Brotkorb, gute Butter, Marmelade, Honig, Tomate-Mozarella Sticks, große Auswahl an Wurst- und Käsevariationen, 2 Scheiben Lachs, Tomate/Mozarella, frischkäse, Joghurt mit Obst, 2x Freilandeier, wahlweise O-Saft oder Prosecco (je 0,1l)</p><span>29,00</span></div>
    <div class="desc" style="margin-top:3px"><p>Für 1 Person</p><span>16,50</span></div>
    <h3>Bambini Frühstück (bis 12 Jahre)</h3>
    <div class="desc"><p>Ein kleines Müsli oder Knusperflocken mit Milch und einer Nacherei</p><span>2,70</span></div>
    <div class="head-row" style="margin-top:5px"><span>Filterkaffee / Tee bis zum „Gehtnichtmehr“</span><span>6,50</span></div>
    <div class="head-row"><span>zzgl. Orangensaft 0,1 l</span><span>1,50</span></div>
    <div class="desc" style="margin-top:5px"><p>Zusätzliches Gedeck für den „Frühstücksteller“</p></div>
  </div>

  <div class="col" style="left:237px;width:113px">
    <h3>Extras nur zum Frühstücksteller</h3>
    <div class="row"><span>Bio-Brötchen</span><span class="price">1,00</span></div>
    <div class="row"><span>Bio-Brötchen Mehrkorn/Dinkel</span><span class="price">1,30</span></div>
    <div class="row"><span>Croissant</span><span class="price">1,50</span></div>
    <div class="row"><span>Port. Butter/Margarine</span><span class="price">1,00</span></div>
    <div class="row"><span>Port. Honig</span><span class="price">1,00</span></div>
    <div class="row"><span>Port. Nussnougat</span><span class="price">1,00</span></div>
    <div class="row"><span>Port. hausgemachte Marmelade</span><span class="price">1,00</span></div>
    <div class="row"><span>2 Scheiben Knäckebrot</span><span class="price">1,00</span></div>
    <div class="row"><span>Gem. Brotkorb</span><span class="price">4,00</span></div>
    <div class="row"><span>Port. Käse (Gouda)</span><span class="price">1,70</span></div>
    <div class="row"><span>Port. Sommersalami</span><span class="price">1,90</span></div>
    <div class="row"><span>Port. Landschinken</span><span class="price">2,20</span></div>
    <div class="row"><span>Port. ital. Käse</span><span class="price">2,70</span></div>
    <div class="row"><span>Port. ital. Salami</span><span class="price">2,70</span></div>
    <div class="row"><span>Port. ital. Mortadella</span><span class="price">2,70</span></div>
    <div class="row"><span>Port. ital. Spezialkäse</span><span class="price">2,90</span></div>
    <div class="row"><span>Port. ital. Fenchelsalami</span><span class="price">2,90</span></div>
    <div class="row"><span>Port. ital. Landschinken</span><span class="price">3,00</span></div>
  </div>

  <div class="col" style="left:374px;width:110px;top:163px">
    <div class="row"><span>Port. Rührei (3 Eier)</span><span class="price">3,90</span></div>
    <div class="row"><span>Port. Rührei mit Kräutern</span><span class="price">4,30</span></div>
    <div class="row"><span>1 Freilandei</span><span class="price">1,20</span></div>
    <div class="row"><span>Frischer Obstsalat</span><span class="price">4,00</span></div>
    <div class="row"><span>Bio-Joghurt mit Obstsalat</span><span class="price">4,70</span></div>
    <div class="row"><span>Bio-Müsli mit Milch</span><span class="price">4,70</span></div>
    <div class="row"><span>Gemüsesticks mit Frischk.</span><span class="price">4,30</span></div>
    <div class="row"><span>Frischkäse, hausgemacht</span><span class="price">1,50</span></div>
    <div class="row"><span>Frischkäse mit Kräutern</span><span class="price">1,70</span></div>
    <div class="row"><span>Port. Ziegenkäse, Scheiben</span><span class="price">2,20</span></div>
    <div class="row"><span>Port. Ziegenfrischkäse</span><span class="price">2,20</span></div>
    <div class="row"><span>Lachs/Sahnemeerettich</span><span class="price">6,50</span></div>
    <div class="row"><span>Port. ital. Camembert</span><span class="price">2,00</span></div>
    <div class="row"><span>Port. veganer Käse</span><span class="price">2,50</span></div>
    <div class="row"><span>Port. veganer Aufschnitt</span><span class="price">2,50</span></div>
    <div class="row"><span>Port. veganer Aufstrich</span><span class="price">2,50</span></div>
    <div class="row"><span>Tomate-Mozarella-Sticks</span><span class="price">4,40</span></div>
    <div class="row"><span>Zusätzliches Gedeck</span><span class="price">1,50</span></div>
  </div>

  <div class="col" style="left:543px;width:121px">
    <h3>Kaffee</h3>
    <div class="row"><span>Filterkaffee klein</span><span class="price">2,20</span></div>
    <div class="row"><span>Filterkaffee groß</span><span class="price">2,80</span></div>
    <div class="row"><span>Filterkaffee endlos bis 12 Uhr</span><span class="price">6,50</span></div>
    <div class="row"><span>Café Creme</span><span class="price">2,50</span></div>
    <div class="row"><span>Café Creme groß</span><span class="price">3,90</span></div>
    <div class="row"><span>Espresso</span><span class="price">1,50</span></div>
    <div class="row"><span>Doppelter Espresso</span><span class="price">2,80</span></div>
    <div class="row"><span>Espresso Macchiato</span><span class="price">2,00</span></div>
    <div class="row"><span>Latte Macchiato klein</span><span class="price">3,20</span></div>
    <div class="row"><span>Latte Macchiato groß</span><span class="price">4,20</span></div>
    <div class="row"><span>Cappuccino</span><span class="price">2,90</span></div>
    <div class="row"><span>Café au Lait</span><span class="price">3,90</span></div>
    <h3>Heiße Getränke</h3>
    <div class="row"><span>Glas Milch</span><span class="price">2,50</span></div>
    <div class="row"><span>Schokolade</span><span class="price">2,90</span></div>
    <div class="row"><span>Zitrone</span><span class="price">2,90</span></div>
    <div class="row"><span>Irish Coffee</span><span class="price">5,90</span></div>
    <h3>Eisgetränke</h3>
    <div class="row"><span>Eiskaffee</span><span class="price">5,50</span></div>
    <div class="row"><span>Eisschokolade</span><span class="price">5,50</span></div>
  </div>

  <div class="col" style="left:680px;width:159px;font-size:8.8px;line-height:14.2px">
    <h3>Alkoholfreie Getränke</h3>
    <div class="row"><span>Cola, Orangenlimo, Zitronenlimo 0,2 l</span><span class="price">2,60</span></div>
    <div class="row"><span>Cola, Orangenlimo, Zitronenlimo 0,4 l</span><span class="price">5,00</span></div>
    <div class="row"><span></span><span class="price">3,20</span></div>
    <div class="row"><span>Wasser 0,35 l (Fontalis Quellwasser)</span><span class="price">5,90</span></div>
    <div class="row"><span>Wasser 0,75 l (Fontalis Quellwasser)</span><span class="price">3,00</span></div>
    <div class="row"><span>Div. Säfte 0,2 l (Apfel, Orange, Multivitamin)</span><span class="price">4,20</span></div>
    <div class="row"><span></span><span class="price">4,20</span></div>
    <div class="row"><span>Div. Schorlen (Apfel, Rhabarber, Maracuja)</span><span class="price">0,70</span></div>
    <div class="row"><span>Div. hausgemachte Limonaden 0,4 l</span><span class="price">2,50</span></div>
    <div class="row"><span>Hafer-, Soja- oder laktosefreie Milch</span><span class="price">0,60</span></div>
    <div class="row"><span>Glas Milch</span><span class="price"></span></div>
    <div class="row"><span>Flavour: Zimt, Haselnuss, Vanille, Karamel</span><span class="price">2,90</span></div>
    <h3>Tee</h3>
    <div class="row"><span>„Herr Brandts“ Darjeeling</span><span class="price">2,90</span></div>
    <div class="row"><span>„Frau Wendts“ Jasmine Tee</span><span class="price">2,90</span></div>
    <div class="row"><span>„Herr Timms“ Red Apple</span><span class="price">2,90</span></div>
    <div class="row"><span>„Herr Petersens“ Green Mango</span><span class="price">2,90</span></div>
    <div class="row"><span>„Herr Harmsens“ Pfefferminz</span><span class="price">2,90</span></div>
    <div class="row"><span>„Frau Jessens“ Rooibos Tea</span><span class="price">2,90</span></div>
    <div class="row"><span>„Frau Lorenz“ Edelflower</span><span class="price">2,90</span></div>
    <div class="row"><span>„Herr Möllers“ Chamomile</span><span class="price">2,90</span></div>
  </div>

  <div class="col" style="left:856px;width:136px">
    <h3>Prosecco</h3>
    <div class="row"><span>Prosecco 0,1 l Hausmarke</span><span class="price">3,20</span></div>
    <div class="row"><span>Prosecco Fl. 0,1 l Villa Serra</span><span class="price">6,20</span></div>
    <div class="row"><span>Prosecco Fl. 0,75 l Villa Serra</span><span class="price">20,50</span></div>
    <div class="row"><span>Prosecco auf Eis</span><span class="price">5,20</span></div>
    <div class="gap" style="height:24px"></div>
    <div class="row"><span>Bitter Spritz 0,2 l</span><span class="price">5,80</span></div>
    <div class="row"><span>Hugo 0,2 l</span><span class="price">5,80</span></div>
  </div>
</section>

</body>
</html>
```